Cat Litter Package and Logo Design

We want new package and Logo design for Cat pine wood litter. Name is “OLVO”. It will be sold in pet store, online shop and supermarket. Our slogan is “Cat litter for your cat, the member of our family”. I mean that cat is not just a pet. They like people in our family. The product for cat is must be the best as selected for member of our family.

Package: Plastic bag with 2 sides
Package Dimension: width 35 cm height 50 cm

Important:
1. Customer will know immediately what product is and for.
2. Outstanding from competitors.
3. Easy to recognize the product.

Front side detail:
1. Cat image
2. Logo: Olvo
3. Slogan: Cat litter for your cat, the member of our family.
4. Detail: Pine Wood Cat Litter
5. Main Highlight -> Breeder Selected
6. Main Features -> Non-Clumping / Odor Control / Dust Free / Save Money / Eco Friendly
7. Show real product (pine wood) inside package: Area to show product will be transparent.
8. Net WT 10 L

Back side detail:
1. One bag for 1 cat & 2 months
2. Benefit: Non-Clumping / Odor Control / Dust Free / Save Money / Eco Friendly
3. How to change for using Olvo Pine Wood Litter: Please mix Olvo with the old one. When your cat can be familiar with Olvo. You can use only Olvo in your cat litter tray.
4. Direction
4.1 Fill the litter height for 2 inches.
4.2 Scoop solid waste.
4.3 Shake litter tray for urine sawdust
4.4 Maintain the height of litter for 2 inches.
5. Imported and Distribution by
5.1 QFO Tech Co.,Ltd.
5.2 Email: Quietfernowlstudio@plumbox.net
6. Little text: *Recommended to use with cat litter tray.

Attached:
1. Our competitors packages
2. Real Cat: You can use it on the package. (I have attached many images, you can select it and use for suitable way.)***
3. Cat litter tray: Don’t use this image. It’s just for describe what is cat litter tray. I prefer drawing.
4. Real product: pine wood

Note: Cat litter is for cat toilet. It's not cat's food.

Target Market(s)

Cat owners whose cats use a litter tray

Industry/Entity Type

Pet

Logo Text

OLVO

Requirements
Must have
• 1. Customer will know immediately what product is and for.
• 2. Outstanding from competitors.
• 3. Easy to recognize the product.

```html
<!DOCTYPE html>
<html lang="en">
<head>
<meta charset="utf-8">
<title>OLVO Pine Wood Cat Litter – Front Package</title>
<link rel="stylesheet" href="https://fonts.googleapis.com/css2?family=Amatic+SC:wght@400;700&family=Lato:ital,wght@0,400;0,700;0,900;1,700&display=swap">
<style>
  :root {
    --page: #ffffff;
    --bag-top: #dcd5b6;
    --bag-mid: #cfc5a1;
    --bag-low: #8c7958;
    --bag-bottom: #5e4e36;
    --ribbon: #c7c23a;
    --ribbon-dash: #4a4620;
    --band: #3d3a1d;
    --band-text: #f4eba4;
    --ink-dark: #3a391c;
    --logo: #4b4a22;
    --slogan: #aea447;
    --net: #f2e8a9;
    --photo-light: #cbbd97;
    --photo-mid: #a48a62;
    --photo-dark: #5c4a33;
    --tray-rim: #e7e79a;
    --pellet-light: #d9bf8e;
    --pellet-dark: #a98552;
  }
  * { box-sizing: border-box; margin: 0; padding: 0; }
  html, body {
    width: 933px; height: 1200px; overflow: hidden;
    background: var(--page);
  }
  .canvas { position: relative; width: 933px; height: 1200px; }
  .package-front {
    position: absolute; left: 95px; top: 68px;
    width: 743px; height: 1092px; overflow: hidden;
    background: linear-gradient(180deg, var(--bag-top) 0%, var(--bag-mid) 45%, var(--bag-low) 80%, var(--bag-bottom) 100%);
  }
  .brand {
    position: absolute; left: 55px; top: 52px;
    font-family: "Lato", sans-serif; font-weight: 900;
    font-size: 84px; letter-spacing: 4px; line-height: 1;
    color: var(--logo);
  }
  .slogan {
    position: absolute; left: 55px; top: 178px;
    font-family: "Lato", sans-serif; font-weight: 700; font-style: italic;
    font-size: 15px; line-height: 1.45; text-transform: uppercase;
    color: var(--slogan);
  }
  .cat-photo {
    position: absolute; left: 18px; top: 250px; width: 380px; height: 842px;
    background: radial-gradient(ellipse 55% 60% at 45% 45%, var(--photo-light) 0%, var(--photo-mid) 55%, var(--photo-dark) 100%);
    border-radius: 48% 48% 0 0 / 22% 22% 0 0;
    opacity: .9;
  }
  .ribbon { position: absolute; left: 445px; top: 0; width: 275px; height: 667px; }
  .product-title {
    position: absolute; left: 445px; top: 68px; width: 275px;
    text-align: center;
    font-family: "Amatic SC", cursive; font-weight: 700;
    font-size: 72px; line-height: 86px; color: var(--ink-dark);
  }
  .highlight-band {
    position: absolute; left: 410px; top: 265px; width: 315px; height: 102px;
    background: var(--band);
    display: flex; flex-direction: column; justify-content: center; align-items: center;
    font-family: "Lato", sans-serif; font-weight: 700;
    font-size: 35px; letter-spacing: 3px; line-height: 42px;
    color: var(--band-text);
  }
  .features {
    position: absolute; left: 445px; top: 380px; width: 275px;
    list-style: none; text-align: center;
    font-family: "Amatic SC", cursive; font-weight: 400;
    font-size: 27px; line-height: 33px; letter-spacing: 1px;
    color: var(--ink-dark);
  }
  .window {
    position: absolute; left: 328px; top: 706px; width: 388px; height: 306px;
    border-radius: 44% 40% 46% 42% / 46% 44% 50% 48%;
    background: radial-gradient(ellipse at 60% 40%, var(--pellet-light) 0%, var(--pellet-dark) 75%);
    border: 22px solid var(--tray-rim);
  }
  .net-weight {
    position: absolute; left: 57px; top: 983px;
    font-family: "Lato", sans-serif; font-weight: 700;
    font-size: 23px; letter-spacing: 1.5px; color: var(--net);
  }
</style>
</head>
<body>
<main class="canvas">
  <section class="package-front">
    <div class="cat-photo" role="img" aria-label="Photo of a tabby and white cat sitting beside an orange ball"></div>

    <div class="brand">OLVO</div>
    <p class="slogan">Cat litter for your cat,<br>the member of our family.</p>

    <svg class="ribbon" viewBox="0 0 275 667" aria-hidden="true">
      <polygon points="0,0 275,0 275,560 137.5,667 0,560" fill="var(--ribbon)"/>
      <polyline points="17,0 17,550 137.5,645 258,550 258,0" fill="none" stroke="var(--ribbon-dash)" stroke-width="2" stroke-dasharray="12 8"/>
    </svg>

    <h1 class="product-title">Pine Wood<br>Cat Litter</h1>

    <div class="highlight-band"><span>BREEDER</span><span>SELECTED</span></div>

    <ul class="features">
      <li>Non-Clumping</li>
      <li>Odor Control</li>
      <li>Dust Free</li>
      <li>Save Money</li>
      <li>Eco Friendly</li>
    </ul>

    <div class="window" role="img" aria-label="Litter tray drawing filled with pine wood pellets, shown through a clear window"></div>

    <p class="net-weight">NET WT 10 L</p>
  </section>
</main>
</body>
</html>
```